RK Tannery Construction Inc.

Design a new business card for our construction company
To be removed from current card:
Delete 25 years
Delete Tenant fit up Renovations section

```html
<!DOCTYPE html>
<html lang="en">
<head>
<meta charset="utf-8">
<title>RK Tannery Construction Inc. – Business Card</title>
<link rel="stylesheet" href="https://fonts.googleapis.com/css2?family=Montserrat:wght@800&family=Open+Sans:wght@400&display=swap">
<style>
  :root {
    --bg: #e9e6ee;
    --purple-deep: #2a0f4a;
    --purple: #4a1f74;
    --purple-light: #5a2e86;
    --paper: #f4f4f4;
    --ink: #3d1a63;
    --text: #3a3a3a;
    --white: #ffffff;
  }
  * { box-sizing: border-box; margin: 0; padding: 0; }
  html, body { width: 1200px; height: 900px; overflow: hidden; }
  body {
    background: var(--bg);
    display: flex;
    flex-direction: column;
    align-items: center;
    justify-content: center;
    gap: 40px;
  }
  .card {
    position: relative;
    width: 700px;
    height: 400px;
    overflow: hidden;
    box-shadow: 0 10px 30px rgba(40, 20, 60, 0.25);
  }
  .card-front {
    background: radial-gradient(ellipse at 50% 45%, var(--purple-light) 0%, var(--purple) 45%, var(--purple-deep) 100%);
    display: flex;
    align-items: center;
    justify-content: center;
  }
  .brand {
    font-family: "Montserrat", sans-serif;
    font-weight: 800;
    text-transform: uppercase;
    line-height: 1;
  }
  .card-front .brand { color: var(--white); text-align: left; }
  .brand-name { display: block; font-size: 58px; letter-spacing: -1px; }
  .brand-sub { display: block; font-size: 27px; letter-spacing: 4px; margin-top: 4px; }

  .card-back { background: var(--paper); }
  .card-back .panels { position: absolute; inset: 0; width: 100%; height: 100%; }
  .card-back .brand {
    position: absolute;
    left: 34px;
    top: 66px;
    color: var(--ink);
  }
  .card-back .brand-name { font-size: 46px; }
  .card-back .brand-sub { font-size: 21px; letter-spacing: 3px; }
  .person {
    position: absolute;
    left: 58px;
    top: 206px;
    font-family: "Montserrat", sans-serif;
    font-weight: 800;
    font-size: 20px;
    letter-spacing: 1px;
    color: var(--ink);
    text-transform: uppercase;
  }
  .contacts {
    position: absolute;
    left: 58px;
    top: 252px;
    list-style: none;
    font-family: "Open Sans", sans-serif;
    font-size: 17px;
    color: var(--text);
  }
  .contacts li { display: flex; align-items: center; gap: 10px; height: 28px; }
  .contacts svg { width: 16px; height: 16px; fill: none; stroke: var(--ink); stroke-width: 1.6; }
  .address {
    position: absolute;
    right: 34px;
    bottom: 46px;
    text-align: right;
    font-family: "Open Sans", sans-serif;
    font-size: 17px;
    line-height: 1.5;
    color: var(--white);
  }
</style>
</head>
<body>
  <section class="card card-front">
    <div class="brand">
      <span class="brand-name">RK Tannery</span>
      <span class="brand-sub">Construction Inc.</span>
    </div>
  </section>

  <section class="card card-back">
    <svg class="panels" viewBox="0 0 700 400" preserveAspectRatio="none" aria-hidden="true">
      <defs>
        <radialGradient id="panelGlow" cx="0.7" cy="0.6" r="0.7">
          <stop offset="0" stop-color="#5a2e86"/>
          <stop offset="0.5" stop-color="#4a1f74"/>
          <stop offset="1" stop-color="#2a0f4a"/>
        </radialGradient>
        <linearGradient id="foldShade" x1="0" y1="0" x2="1" y2="0">
          <stop offset="0" stop-color="#2a0f4a"/>
          <stop offset="1" stop-color="#3d1a63"/>
        </linearGradient>
      </defs>
      <polygon points="330,0 700,0 700,400 470,400" fill="url(#panelGlow)"/>
      <polygon points="330,0 420,30 470,400 445,400 395,40" fill="url(#foldShade)"/>
      <polygon points="300,0 330,0 420,30 395,40" fill="#3a1760"/>
      <line x1="420" y1="30" x2="470" y2="400" stroke="#1e0838" stroke-width="2"/>
    </svg>

    <div class="brand">
      <span class="brand-name">RK Tannery</span>
      <span class="brand-sub">Construction Inc.</span>
    </div>

    <p class="person">Dylan Tannery</p>

    <ul class="contacts">
      <li>
        <svg viewBox="0 0 16 16"><rect x="4" y="1" width="8" height="14" rx="1.5"/><line x1="7" y1="12.5" x2="9" y2="12.5"/></svg>
        613-555-0142
      </li>
      <li>
        <svg viewBox="0 0 16 16"><path d="M2 6c0-2 3-3 6-3s6 1 6 3v1h-3V5.5H5V7H2z"/><rect x="3" y="8" width="10" height="6" rx="1"/></svg>
        613-555-0190 ext.221
      </li>
      <li>
        <svg viewBox="0 0 16 16"><rect x="1.5" y="3.5" width="13" height="9" rx="1"/><polyline points="1.5,4 8,9 14.5,4"/></svg>
        dylan@rktanneryconstruction.ca
      </li>
      <li>
        <svg viewBox="0 0 16 16"><circle cx="8" cy="8" r="6.5"/><ellipse cx="8" cy="8" rx="2.8" ry="6.5"/><line x1="1.5" y1="8" x2="14.5" y2="8"/></svg>
        www.rktanneryconstruction.ca
      </li>
    </ul>

    <address class="address" style="font-style: normal;">
      1280 Birchmount Rd.<br>
      Suite 200, Ottawa<br>
      ON K2B7X4
    </address>
  </section>
</body>
</html>
```